Business Card and Logo Color Scheme Design Contest

We are starting a new company called Lone Ridge Structural Partners and already have a logo however, the colors for the logo itself are not final and COULD be changed. I'm hoping to move AWAYfrom the gold color in the card and the logo as it seems a bit outdated. What we need help with is to find what our business color scheme will be, and then incorporate those colors into both the logo and the business card design itself. We also want to make sure we are known as "LRS" so in the future we can just refer to ourselves as "LRS" and not Lone Ridge Structural Partners. That being said, I would like to make a slight change to the logo to somehow include the letters "LRS." The logo used in the front of the card design MUST ALSO include the words "Firm No. 64307" within the logo. My vision is for the front of the card to have the information shown in the attached image. For the back of the card, I'm hoping to have something very simple. I'm envisioning a solid color with either the website (www.bridgemarkplans.com) and a simplified version of the logo. I've attached an example but I'm looking for a complete redesign. I'm looking for a slick, modern and simple design.

Industry/Entity Type

Civil Engineer

Contact Information for Business Card

Logo
Firm No. 64307
Reid Tamsworth, PE
Chief Operating Officer
Email:rtamsworth@bridgemarkplans.com
Ph: 936.555.0142 | D: 936.555.0178 | M:210.555.0263
4187 W. Kellingham, Conroe, Texas 77301
www.bridgemarkplans.com

Requirements
Must have
• Logo
Contact Info
Nice to have
• "LRS" Incorporated in the design
Should not have
• The current color scheme

```html
<!DOCTYPE html>
<html lang="en">
<head>
<meta charset="utf-8">
<title>Lone Ridge Structural Partners Business Card</title>
<link href="https://fonts.googleapis.com/css2?family=Barlow:wght@400;600;700&display=swap" rel="stylesheet">
<style>
  :root {
    --navy: #1a1f3f;
    --white: #ffffff;
    --backdrop: #4a5274;
    --ink: #1a1f3f;
  }
  * { margin: 0; padding: 0; box-sizing: border-box; }
  html, body { width: 1200px; height: 1200px; overflow: hidden; }
  body {
    background: var(--backdrop);
    font-family: "Barlow", Arial, sans-serif;
    position: relative;
  }
  .card { position: absolute; }
  .card-front {
    left: 286px;
    top: 204px;
    width: 630px;
    height: 360px;
    background: var(--navy);
    color: var(--white);
  }
  .brand {
    position: absolute;
    top: 164px;
    left: 0; right: 0;
    display: flex;
    justify-content: center;
    align-items: center;
    gap: 10px;
  }
  .brand-mark {
    width: 14px;
    height: 14px;
    background: var(--white);
  }
  .brand-name {
    font-weight: 700;
    font-size: 22px;
    line-height: 24px;
    letter-spacing: 1px;
    text-transform: uppercase;
  }
  .brand-firm {
    position: absolute;
    top: 198px;
    left: 0; right: 0;
    text-align: center;
    font-weight: 700;
    font-size: 10px;
    letter-spacing: 1px;
    text-transform: uppercase;
  }
  .card-back {
    left: 285px;
    top: 620px;
    width: 636px;
    height: 364px;
    background: var(--white);
    color: var(--ink);
  }
  .person {
    position: absolute;
    top: 88px;
    left: 0; right: 0;
    text-align: center;
  }
  .person-name {
    font-weight: 700;
    font-size: 22px;
    line-height: 26px;
    letter-spacing: 0.3px;
  }
  .person-title {
    font-weight: 400;
    font-size: 19px;
    line-height: 22px;
    letter-spacing: 0.5px;
  }
  .phones {
    position: absolute;
    left: 37px;
    top: 209px;
    font-size: 16px;
    line-height: 21.5px;
  }
  .phones .label { display: inline-block; width: 30px; }
  .phones strong { font-weight: 700; }
  .address {
    position: absolute;
    right: 40px;
    top: 209px;
    text-align: right;
    font-size: 16px;
    line-height: 21.5px;
  }
  .icon { width: 12px; height: 12px; vertical-align: -1px; margin-left: 4px; }
  .web-band {
    position: absolute;
    left: 0; right: 0;
    top: 300px;
    height: 41px;
    background: var(--navy);
    color: var(--white);
    text-align: right;
    padding-right: 40px;
    font-size: 18px;
    line-height: 41px;
    letter-spacing: 0.5px;
  }
</style>
</head>
<body>
  <section class="card card-front">
    <div class="brand">
      <span class="brand-mark" aria-hidden="true"></span>
      <span class="brand-name">Lone Ridge Structural Partners</span>
    </div>
    <div class="brand-firm">Firm No. 64307</div>
  </section>

  <section class="card card-back">
    <div class="person">
      <div class="person-name">REID TAMSWORTH, PE</div>
      <div class="person-title">Chief Operating Officer</div>
    </div>
    <div class="phones">
      <div><span class="label">Ph:</span><strong>936.555.0142</strong></div>
      <div><span class="label">D&nbsp; :</span><strong>936.555.0178</strong></div>
      <div><span class="label">M :</span><strong>210.555.0263</strong></div>
    </div>
    <div class="address">
      <div>4187 W. Kellingham</div>
      <div>Conroe, Texas 77301</div>
      <div>rtamsworth@bridgemarkplans.com<svg class="icon" viewBox="0 0 12 12" aria-hidden="true"><rect x="0.75" y="2.25" width="10.5" height="7.5" rx="1" fill="none" stroke="currentColor" stroke-width="1.3"/><path d="M1 3 L6 6.8 L11 3" fill="none" stroke="currentColor" stroke-width="1.3"/></svg></div>
    </div>
    <div class="web-band">www.bridgemarkplans.com<svg class="icon" viewBox="0 0 12 12" aria-hidden="true"><circle cx="6" cy="6" r="5.5" fill="currentColor"/><path d="M3 4 Q5 3 6 5 Q5 7 7 8 L6 10 M8 3 Q9.5 4 9 6" fill="none" stroke="#1a1f3f" stroke-width="1.2"/></svg></div>
  </section>
</body>
</html>
```